event catering company brochure & menus

i have a collaboration of different menus that i would like redesigning each one for expanding my company to the uae

Along with this i would like them to be formatted into a brochure to use & photos attached to what is suitable

Target Market(s)

corperate customers

Industry/Entity Type

catering

```html
<!DOCTYPE html>
<html lang="en">
<head>
<meta charset="utf-8">
<title>Valentessa – Catering Brochure Spread</title>
<link rel="stylesheet" href="https://fonts.googleapis.com/css2?family=Lato:wght@300;400;700&display=swap">
<style>
  :root {
    --backdrop: #ececec;
    --blush: #c99b90;
    --blush-deep: #bf8f84;
    --blush-light: #e2b8ad;
    --ink-light: #fbf1ee;
    --accent-red: #b2473c;
    --gold-1: #b8912e;
    --gold-2: #f3dc7a;
    --gold-3: #d9b548;
    --gold-4: #fff1a8;
    --food-1: #e9e4dc;
    --food-2: #7aa145;
    --table-1: #f1efec;
    --table-2: #b9c3b5;
  }
  * { box-sizing: border-box; margin: 0; padding: 0; }
  html, body { width: 1200px; height: 749px; overflow: hidden; }
  body {
    background: var(--backdrop);
    font-family: "Lato", Arial, sans-serif;
    position: relative;
  }
  .spread {
    position: absolute;
    left: 40px; top: 95px;
    width: 1120px; height: 560px;
    display: flex;
    box-shadow: 0 14px 30px rgba(0,0,0,0.12);
  }
  .page {
    position: relative;
    width: 560px; height: 560px;
    background: var(--blush);
    overflow: hidden;
  }
  .page--left { background: linear-gradient(90deg, var(--blush) 88%, var(--blush-deep)); }
  .page--right { background: linear-gradient(90deg, var(--blush-deep), var(--blush) 12%); }

  .gold {
    position: absolute;
    background: linear-gradient(120deg, var(--gold-1), var(--gold-2) 25%, var(--gold-3) 45%, var(--gold-4) 65%, var(--gold-1) 85%, var(--gold-2));
  }
  .gold--top { top: 0; left: 0; right: 0; height: 14px; }
  .gold--bottom { bottom: 0; left: 0; right: 0; height: 14px; }
  .gold--left { top: 0; bottom: 0; left: 0; width: 14px; }
  .gold--right { top: 0; bottom: 0; right: 0; width: 14px; }

  .wordmark {
    position: absolute;
    font-weight: 300;
    color: var(--gold-3);
    text-transform: uppercase;
    letter-spacing: 0.42em;
    line-height: 1;
  }
  .page--left .wordmark { left: 34px; top: 26px; font-size: 42px; }
  .page--right .wordmark { right: 40px; top: 34px; font-size: 40px; }

  .tagline {
    position: absolute;
    left: 34px; top: 76px;
    font-size: 17px;
    font-weight: 300;
    color: var(--ink-light);
    text-transform: uppercase;
    letter-spacing: 0.02em;
  }

  .photo { position: absolute; }
  .photo--dish {
    left: 14px; top: 105px; width: 240px; height: 360px;
    background: radial-gradient(circle at 55% 55%, var(--food-2) 0 18%, #e3a66a 30%, var(--food-1) 60%);
  }
  .photo--table {
    right: 14px; top: 125px; width: 200px; height: 421px;
    background: linear-gradient(160deg, #c9bfb3, var(--table-1) 40%, var(--table-2) 70%, var(--table-1));
  }
  .gold--photo-left { left: 254px; top: 105px; width: 10px; height: 360px; }
  .gold--photo-right { right: 214px; top: 125px; width: 10px; height: 421px; }

  .body-copy {
    font-size: 11px;
    line-height: 1.4;
    color: var(--ink-light);
    text-align: justify;
  }
  .intro {
    position: absolute;
    left: 282px; top: 118px; width: 250px;
  }

  .services {
    position: absolute;
    left: 48px; top: 92px; width: 280px;
  }
  .services__title {
    font-size: 17px; font-weight: 300;
    color: var(--ink-light);
    text-transform: uppercase;
    letter-spacing: 0.05em;
    margin-left: 118px;
    margin-bottom: 10px;
  }
  .service__heading {
    font-size: 18px; font-weight: 300;
    color: var(--ink-light);
    text-transform: uppercase;
    margin-bottom: 8px;
  }
  .service { margin-bottom: 22px; }

  .coverage {
    position: absolute;
    left: 48px; top: 440px; width: 268px;
    background: var(--blush-light);
    padding: 10px 14px;
    font-size: 12px;
    line-height: 1.3;
    color: var(--accent-red);
    text-align: justify;
  }
</style>
</head>
<body>
  <main class="spread">
    <section class="page page--left">
      <div class="gold gold--top"></div>
      <div class="gold gold--left"></div>
      <div class="gold gold--bottom"></div>

      <h1 class="wordmark">Valentessa</h1>
      <p class="tagline">Servicing across the UAE &amp; Middle East</p>

      <div class="photo photo--dish" role="img" aria-label="Plated salmon fillet with dill, asparagus spears, a poached egg yolk, herb oil and toasted crumb"></div>
      <div class="gold gold--photo-left"></div>

      <p class="body-copy intro">A great dining experience should leave more than a great taste in your mouth. That's why Valentessa Events combine the best flavours with outstanding customer service to deliver exclusive dining experiences. Whether you're looking for a caterer in Dubai, Abu Dhabi or Ras al Khaimah, a private chef for an intimate dinner or an events partner, our team has been creating menus since 2012. Having grown a reputation across the United Kingdom, we have expanded our operation throughout the Middle East. Whether you are looking to impress clients at a corporate launch or planning a dinner party in your home, we bring the same care to every detail. Our experienced team brings your ideas to life, with a service tailored to you and a discreet, unobtrusive yet responsive style.</p>
    </section>

    <section class="page page--right">
      <div class="gold gold--top"></div>
      <div class="gold gold--right"></div>
      <div class="gold gold--bottom"></div>

      <h2 class="wordmark">Valentessa</h2>

      <div class="services">
        <h3 class="services__title">Services</h3>
        <article class="service">
          <h4 class="service__heading">Private Dining</h4>
          <p class="body-copy">Create a restaurant dining experience in the comfort of your own private residence with our private dining catering service. We bring a high end restaurant into your home offering the utmost exclusivity and privacy. Let the team take care of every last detail of designing the menu &amp; transforming your dining room into a restaurant setting whilst you sit back, relax and enjoy the luxury of being catered for by our experienced chefs and hosted by our friendly waiting team.</p>
        </article>
        <article class="service">
          <h4 class="service__heading">Event Catering</h4>
          <p class="body-copy">Experience the gastronomic excellence reflected in our menus, with each dish designed with your style and theme in mind. From showroom launches through to corporate events in the desert, birthdays, anniversaries and seasonal holidays, our food will be tailored to you, your guests and your occasion.</p>
        </article>
      </div>

      <p class="coverage">We cover every corner of the Middle East including Dubai, Abu Dhabi, Ras al-Khaimah, Saudi Arabia, Qatar &amp; Oman.</p>

      <div class="gold gold--photo-right"></div>
      <div class="photo photo--table" role="img" aria-label="Banquet table laid with wine glasses, white plates, cutlery and sharing platters of salad"></div>
    </section>
  </main>
</body>
</html>
```